Holistic Therapy (aromatherapy, massage, reflexology, life coaching, soul healing, aura reading)

I work for myself as a holistic therapist doing: aromatherapy massage, massage, reflexology, abdominal-sacral massage, life coaching, soul healing, aura readings. I want a business card that doesn't focus on any one of these( so not just feet or a massage couch,but rather a card that creates the feeling of wholeness, healing, health and which can encompass all my therapies - e.g. green or purple are colours I like (especially green, or maybe green on back and purple on front). It's going to be called Rosa Pell Therapies. I don't want to list all my therapies on the card in case I add others later.). At some point I will create a website but in this instance I just want to get some cards printed to get 'out there' while I design my website.

Hi, thanks for all your designs. Can you find a way to include the therapies that I offer within the card, either on the front or back…the therapies I offer are: aromatherapy massage, reflexology, swedish body massage, abdominal-sacral massage, nutrition, soul healing, aura readings. (Maybe have them with a bullet point before each?) I am not sure whether they should be on the front of the card or the back or whether having them would spoil the card but it occurred to me that just having rosa pell therapies doesn't tell people what therapies I offer, hence the new idea to list them somehow…)

Target Market(s)

Mainly women (middle class probably with disposable incomes).

Industry/Entity Type

Massage

Contact Information for Business Card

Rosa Pell Therapies, Tel: 07700 900482, email: lumacrest@postvane.com, (on back of card I want: Rosalind Pell BScHons, CPWRA, RGPC.)

Requirements
Nice to have
• A logo for Rosa Pell Therapies would be good.

```html
<!DOCTYPE html>
<html lang="en">
<head>
<meta charset="utf-8">
<title>Rosa Pell Therapies – Business Card</title>
<link rel="stylesheet" href="https://fonts.googleapis.com/css2?family=Tillana:wght@400;500&display=swap">
<style>
  :root {
    --card-bg: #e9fde0;
    --leaf-green: #3aec14;
    --emblem-light: #b4f08f;
    --emblem-deep: #4fdc25;
    --card-width: 1200px;
    --card-height: 791px;
  }

  html, body {
    margin: 0;
    padding: 0;
    width: var(--card-width);
    height: var(--card-height);
    overflow: hidden;
    background: var(--card-bg);
  }

  .business-card {
    position: relative;
    width: var(--card-width);
    height: var(--card-height);
    background: var(--card-bg);
    font-family: "Tillana", "Gabriola", cursive;
    color: var(--leaf-green);
    text-align: center;
  }

  .brand-emblem {
    position: absolute;
    left: 450px;
    top: 106px;
    width: 300px;
    height: 300px;
  }

  .brand-name {
    position: absolute;
    left: 0;
    right: 0;
    top: 404px;
    margin: 0;
    font-size: 74px;
    font-weight: 400;
    line-height: 1;
    letter-spacing: 0.5px;
  }

  .contact-list {
    position: absolute;
    left: 0;
    right: 0;
    top: 532px;
    margin: 0;
    padding: 0;
    list-style: none;
    font-size: 38px;
    line-height: 68px;
  }
</style>
</head>
<body>
  <main class="business-card">
    <svg class="brand-emblem" viewBox="0 0 300 300" role="img" aria-label="Circular brand emblem with flowing swirl pattern">
      <defs>
        <radialGradient id="emblem-fill" cx="50%" cy="45%" r="55%">
          <stop offset="0%" stop-color="var(--emblem-light)"/>
          <stop offset="100%" stop-color="var(--emblem-deep)"/>
        </radialGradient>
      </defs>
      <circle cx="150" cy="150" r="148" fill="url(#emblem-fill)"/>
    </svg>

    <h1 class="brand-name">Rosa Pell Therapies</h1>

    <ul class="contact-list">
      <li class="contact-phone">Tel: 07700 900482</li>
      <li class="contact-email">Email: lumacrest@postvane.com</li>
    </ul>
  </main>
</body>
</html>
```